Business card design needed

We are 2 artists starting up a studio by the water in Sydney ...where we can work and display our art...would like the back ground to be Navy and white stripe...nautical...and the name The Paint Hut to be bold and the main wording...not nautical...if possible thought the A for art could be an easel ...ie the capital A using the cross bar as the platform that paint would be circles of colour....would like the main wording in Black but the easel A in colour
Hope u are able to help
thanku Lorna Vesk
as I will be away in a week for 4 weeks could u please send all info to Mira Colbins email....she can contact me and we can go ahead asap....

Artists

THE PAINT HUT

Hallorans Oar House
The Reach..17 Kellaby Rd..Dunrook 2091 Sydney

Mir Colbin..0437819025..miracolbin@mailnest.example
Lorn Vesk...0429573816..lvesk@harborlink.example

```html
<!DOCTYPE html>
<html lang="en">
<head>
<meta charset="utf-8">
<title>The Paint Hut – Business Card</title>
<link rel="stylesheet" href="https://fonts.googleapis.com/css2?family=Arimo:wght@400;700&display=swap">
<style>
  :root {
    --stripe-top: #5b4679;
    --stripe-bottom: #2c2946;
    --navy: #2d2b48;
    --white: #ffffff;
    --paper: #ffffff;
    --frame: #d9d9d9;
    --ink: #333333;
  }
  html, body {
    margin: 0;
    padding: 0;
    overflow: hidden;
    background: var(--white);
  }
  .card {
    position: relative;
    width: 1200px;
    height: 677px;
    background: var(--white);
    overflow: hidden;
    font-family: "Arimo", Arial, sans-serif;
  }
  .stripe {
    position: absolute;
    left: 0;
    width: 100%;
    background: linear-gradient(to bottom, var(--stripe-top), var(--stripe-bottom));
  }
  .stripe--one { top: 41px; height: 75px; }
  .stripe--two { top: 180px; height: 74px; }
  .stripe--three { top: 320px; height: 76px; }

  .name-panel {
    position: absolute;
    left: 369px;
    top: 55px;
    width: 446px;
    height: 329px;
    box-sizing: border-box;
    background: var(--paper);
    border: 7px solid var(--frame);
    border-radius: 12px;
    box-shadow: 0 4px 8px rgba(0,0,0,0.25);
    display: flex;
    flex-direction: column;
    align-items: center;
    justify-content: center;
  }
  .studio-name {
    margin: 0;
    color: var(--ink);
    font-weight: 700;
    font-size: 68px;
    line-height: 1.05;
    text-align: center;
  }

  .contact-band {
    position: absolute;
    left: 0;
    top: 440px;
    width: 100%;
    height: 237px;
    background: var(--navy);
    color: var(--white);
  }
  .contact {
    position: absolute;
    top: 56px;
    margin: 0;
    font-size: 25px;
    line-height: 33px;
    font-style: normal;
  }
  .contact--studio { left: 56px; }
  .contact--artist { left: 815px; top: 50px; }
  .contact strong {
    display: block;
    font-weight: 700;
    font-size: 26px;
  }
</style>
</head>
<body>
  <div class="card">
    <div class="stripe stripe--one"></div>
    <div class="stripe stripe--two"></div>
    <div class="stripe stripe--three"></div>

    <div class="name-panel">
      <p class="studio-name">The Paint<br>Hut</p>
    </div>

    <div class="contact-band">
      <address class="contact contact--studio">
        <strong>THE PAINT HUT</strong>
        Hallorans Oar House The Reach.<br>
        17 Kellaby Rd.<br>
        Dunrook 2091 Sydney Mir Colbin 0437819025
      </address>
      <address class="contact contact--artist">
        <strong>Lorn Vesk</strong>
        miracolbin@mailnest.example<br>
        0429573816<br>
        lvesk@harborlink.example
      </address>
    </div>
  </div>
</body>
</html>
```